Healthcare Shopping and Education

We want to create a theme and story through to educate employees on being better consumers within healthcare. The following area's are where employees and employers are losing a lot of money.

1. Cost Variance-Hospital A might charge $1,000 for a MRI and Hospital B (5 miles away) might charge $4,000. We want to make people aware of not only the cost but the quality.

2. Misdiagnosis-Please see attached file regarding the stats. We need to make people aware the doctors and hospitals make errors

3. Second Opinion-We have the ability to provide second opinions for those that get sick and they don't have to leave their own home-Our clinical nurses take care of everything.

A few theme options that we have are:

• "Don't spend your wealth getting your health"
• "Know before you go"
• "Together we solve healthcare"
• "Be Aware About Your Care"
• “Did you know” campaign? – campaigns that ask questions
• Community solves the healthcare problem - like the "go green" campaign
• "Care Before You Get Care"
• Help a friend (Messaging around helping others - reminder about our services)
• Symbol to carry throughout and create a story
• Health coach, health angel, guard, guide, ally, May Day

We are open to campaigns around any and all of these ideas.
Updates

Please note I'm trying to create a campaign-I'm looking for an idea that I can carry out through multiple pieces not just one piece.

Industry/Entity Type

Healthcare

Font styles to use
Serif

Requirements
Must have
• Engagement Content Summary
The engagement content should create a call to action that focuses on simplicity, savings, and navigation through the healthcare space. It should create a story that is memorable across marketing pieces/tactics and resonates with an employee’s emotions. The content can be summarized in three factors:

Motivation – need to create campaigns and messaging that reminds them they have the services and is memorable so that they use the services when the time comes; messaging should resonate with an employee’s emotions – pleasure, pain, confusion - and create action

Ability – the engagement content should create a call to action and focus on simplicity. For example, one click healthcare, YOUR personal assistant for healthcare, it’s never been so easy.

Trigger – the content should include proactive messaging and direct employees to do something

Nice to have
• This will be around 2-3 designs to start with and then end with a total of 10-15 based on additional hiring and additional payment.

We see this as mini billboards inside buildings to drive awareness about becoming a more educated healthcare consumer-We will provide some additional content to build the design.

Think of this being a campaign that can be carried out through a number of mini billboards.
Should not have
• A lot of words. Boring. Non attention grabbing.

```html
<!DOCTYPE html>
<html lang="en">
<head>
<meta charset="utf-8">
<title>Get an Umbrella – It might rain</title>
<link href="https://fonts.googleapis.com/css2?family=Gelasio:wght@400;500&display=swap" rel="stylesheet">
<style>
  :root {
    --page-white: #ffffff;
    --green-wash: #c8f2a0;
    --yellow-wash: #fbf6b4;
    --center-glow: #fbfbe8;
    --ink-dark: #4a4a4a;
    --ink-heading: #1e1e1e;
    --ink-body: #555555;
    --accent-red: #ff2b2b;
    --title-glow: #f3f08c;
    --umbrella-blue: #2a5ad8;
    --rain-cyan: #40dcec;
  }
  * { margin: 0; padding: 0; box-sizing: border-box; }
  html, body {
    width: 844px; height: 1200px; overflow: hidden;
    background: var(--page-white);
    font-family: "Gelasio", Georgia, serif;
  }
  .billboard {
    position: absolute; left: 21px; top: 21px;
    width: 802px; height: 1158px;
    background:
      radial-gradient(ellipse 260px 300px at 52% 45%, var(--center-glow) 0%, rgba(251,251,232,0) 100%),
      linear-gradient(225deg, var(--green-wash) 0%, #d6f3a6 35%, #f2f5bd 60%, var(--yellow-wash) 100%);
    overflow: hidden;
  }
  .headline {
    position: absolute; left: 40px; top: 88px;
    transform: rotate(-5deg); transform-origin: left top;
    font-weight: 400;
    color: var(--ink-dark);
    text-shadow: 2px 3px 2px var(--title-glow);
    white-space: nowrap;
  }
  .headline-line { display: block; font-size: 52px; line-height: 1; letter-spacing: 1px; }
  .headline-line + .headline-line { margin: 20px 0 0 80px; font-size: 46px; }
  .headline .word-gap { margin-left: 22px; }
  .umbrella { color: var(--umbrella-blue); font-size: 56px; }
  .rain { color: var(--rain-cyan); font-size: 54px; }

  .tips { position: absolute; left: 155px; top: 388px; width: 520px; }
  .tip + .tip { margin-top: 56px; }
  .tip-title { font-size: 24px; font-weight: 400; color: var(--ink-heading); line-height: 1.2; }
  .tip-text { margin-top: 20px; font-size: 17px; line-height: 25px; color: var(--ink-body); }

  .call-to-action {
    position: absolute; left: 82px; top: 855px;
    font-size: 35px; line-height: 44px; color: var(--ink-dark);
  }
  .reassurance { position: absolute; left: 82px; top: 962px; width: 720px; }
  .reassurance-lead {
    position: absolute; left: 0; top: 12px;
    font-size: 31px; color: var(--ink-dark); white-space: nowrap;
  }
  .reassurance-promise {
    position: absolute; left: 411px; top: -6px;
    font-size: 31px; line-height: 42px; color: var(--accent-red); white-space: nowrap;
  }
</style>
</head>
<body>
  <main class="billboard">
    <h1 class="headline">
      <span class="headline-line">Get<span class="word-gap">an</span><span class="word-gap umbrella">Umbrella</span></span>
      <span class="headline-line">It<span class="word-gap">might</span><span class="word-gap rain">rain</span></span>
    </h1>

    <section class="tips">
      <article class="tip">
        <h2 class="tip-title">Quality vs Money</h2>
        <p class="tip-text">Wealth can’t buy Health, but go for the best medical services.</p>
      </article>
      <article class="tip">
        <h2 class="tip-title">A second advice</h2>
        <p class="tip-text">Doctors are humans and Humans can make mistakes. So a<br>second advice from a professional can be life saving.</p>
      </article>
      <article class="tip">
        <h2 class="tip-title">Why go to Hospital</h2>
        <p class="tip-text">There is no place like Home. So why go to Hospital when you<br>can get a clinical nurse to your own home.</p>
      </article>
    </section>

    <p class="call-to-action">It is time to get your own personal<br>assistance for health care.</p>

    <div class="reassurance">
      <p class="reassurance-lead">So when you are in need</p>
      <p class="reassurance-promise">NO RUSH<br>NO WORRIES</p>
    </div>
  </main>
</body>
</html>
```